integrative health clinic-Medical massage, acupuncture, chiropractic

we like our logo, but are open to new ideas. We need a new card design. We have added chiropractic and acupuncture that we have put under the name of the business. We are an integrative medical clinic

Target Market(s)

General public, athletes

Contact Information for Business Card

Phone 5055583927
Fax 5055583926
Hours Monday-Friday 9-6
Saturday 10-6
The 20% can be smaller on the back

Colors
3176b5
0355a3

Requirements
Must have
• Logo but am open to ideas
Nice to have
• We are an integrated medical clinic but also want to be personable. We want the card fun and inviting

```html
<!DOCTYPE html>
<html lang="en">
<head>
<meta charset="utf-8">
<title>Open Harbor Wellness – Business Card</title>
<link href="https://fonts.googleapis.com/css2?family=Oswald:wght@300;400;500&family=Roboto+Condensed:wght@400;700&family=Roboto:wght@500;700&display=swap" rel="stylesheet">
<style>
  :root {
    --blue-light: #3176b5;
    --blue-deep: #0355a3;
    --ink: #1b1b1b;
    --paper: #ffffff;
    --backdrop: #e6e6e6;
    --navy: #0a1a3a;
  }
  * { box-sizing: border-box; margin: 0; padding: 0; }
  html, body { width: 1200px; height: 787px; overflow: hidden; }
  body {
    background: var(--backdrop);
    display: flex;
    align-items: center;
    justify-content: center;
    gap: 40px;
    font-family: "Roboto Condensed", sans-serif;
  }
  .card {
    position: relative;
    width: 560px;
    height: 326px;
    background: var(--paper);
    overflow: hidden;
    box-shadow: 0 4px 14px rgba(0,0,0,0.18);
  }
  .card__shapes { position: absolute; inset: 0; width: 100%; height: 100%; }
  .shape--light { fill: var(--blue-light); }
  .shape--deep { fill: var(--blue-deep); }

  /* Front */
  .front__illustration {
    position: absolute;
    left: 0; top: 0;
    width: 250px; height: 100%;
    background: linear-gradient(150deg, #2f6fc0 0%, var(--navy) 55%, #0d2a66 100%);
  }
  .front__content {
    position: absolute;
    left: 262px; right: 26px; top: 40px; bottom: 20px;
  }
  .brand__name {
    font-family: "Roboto", sans-serif;
    font-weight: 700;
    font-size: 25px;
    color: var(--ink);
    display: flex;
    align-items: center;
    gap: 8px;
  }
  .brand__dot {
    width: 14px; height: 14px; border-radius: 50%;
    background: var(--blue-deep);
    flex: none;
  }
  .brand__tagline {
    font-family: "Roboto Condensed", sans-serif;
    font-size: 11.5px;
    color: var(--ink);
    margin: 4px 0 0 22px;
  }
  .front__specialty {
    text-align: right;
    color: var(--blue-light);
    font-size: 14px;
    line-height: 1.3;
    margin-top: 26px;
  }
  .front__contact {
    text-align: right;
    font-size: 16px;
    color: var(--ink);
    line-height: 1.25;
    margin-top: 22px;
    padding-right: 10px;
  }
  .front__hours {
    position: absolute;
    left: 0; right: 0;
    bottom: 40px;
    text-align: center;
    color: var(--blue-deep);
    font-size: 17px;
    padding-left: 20px;
  }

  /* Back */
  .back__content {
    position: absolute;
    inset: 0;
    display: flex;
    flex-direction: column;
    align-items: center;
    padding-top: 50px;
  }
  .back__book {
    font-family: "Oswald", sans-serif;
    font-weight: 300;
    font-size: 19px;
    color: var(--blue-light);
    letter-spacing: 0.3px;
  }
  .back__brand {
    margin-top: 22px;
    font-family: "Roboto", sans-serif;
    font-weight: 700;
    font-size: 18px;
    color: var(--blue-deep);
    display: flex;
    align-items: center;
    gap: 8px;
  }
  .back__web {
    margin-top: 26px;
    font-size: 16px;
    color: var(--ink);
  }
  .back__offer {
    margin-top: 14px;
    font-family: "Roboto Condensed", sans-serif;
    font-weight: 700;
    font-size: 18px;
    color: var(--blue-deep);
  }
</style>
</head>
<body>

  <section class="card card--front">
    <div class="front__illustration" role="img" aria-label="Illustration of a human skeleton bending forward with the lower spine highlighted in red"></div>
    <svg class="card__shapes" viewBox="0 0 560 326" aria-hidden="true">
      <path class="shape--light" d="M420 0 H470 L440 30 Q432 36 424 28 Z"/>
      <path class="shape--deep" d="M478 0 H560 V110 Q560 118 552 112 L470 24 Q464 16 472 8 Z"/>
      <path class="shape--light" d="M150 326 L196 258 Q204 248 212 258 L258 326 Z"/>
      <path class="shape--deep" d="M0 326 V300 L40 326 Z"/>
    </svg>
    <div class="front__content">
      <div class="brand">
        <div class="brand__name"><span class="brand__dot"></span>Open Harbor Wellness</div>
        <div class="brand__tagline">Sports Therapy and Wellness Center</div>
      </div>
      <p class="front__specialty">Specializing in Medical, Sports Massage<br>and Manual Therapies</p>
      <p class="front__contact">P: 5055583927<br>F: 5055583926</p>
    </div>
    <p class="front__hours" style="left:250px;">Hrs: Monday-Friday 9-6 / Saturday 10-6</p>
  </section>

  <section class="card card--back">
    <svg class="card__shapes" viewBox="0 0 560 326" aria-hidden="true">
      <path class="shape--light" d="M430 0 H500 L470 34 Q462 42 454 34 Z"/>
      <path class="shape--deep" d="M506 0 H560 V92 L494 20 Q488 12 496 6 Z"/>
      <path class="shape--deep" d="M470 326 L552 236 Q560 228 560 240 V326 Z"/>
    </svg>
    <div class="back__content">
      <p class="back__book">BOOK ONLINE</p>
      <div class="back__brand"><span class="brand__dot"></span>Open Harbor Wellness</div>
      <p class="back__web">www.openharborwellnessnm.com</p>
      <p class="back__offer">20% OFF FIRST VISIT</p>
    </div>
  </section>

</body>
</html>
```